Guided Study Tour - Halmerfest Leipzig Two Sided Flyer

We need a two-sided flyer for a Guided Study Tour to Halmerfest Leipzig. We want beautiful pictures of Germany and if possible some of the Halmer venues our participants will be visiting. I have also provided the content that needs to be included. Also, in the attached document I provided a link to the Halmerfest event. Please read and watch the video to be inspired.
This flyer should be beautiful and engaging. It needs to grab your attention right away and really highlight the wonderful things that they will be doing and that are included in the tour. This is a once in a lifetime opportunity for people to experience. We are targeting Music Directors and Music professionals.
Both attached logos need to be present on the flyer.

```html
<!DOCTYPE html>
<html lang="en">
<head>
<meta charset="utf-8">
<title>Guided Study Tour – Halmerfest Leipzig</title>
<link rel="stylesheet" href="https://fonts.googleapis.com/css2?family=Alegreya:wght@400;700&display=swap">
<style>
  :root {
    --brand-blue: #0f86bf;
    --deep-navy: #0b2a5a;
    --ink: #1d1d1d;
    --white: #ffffff;
    --partner-red: #c8202a;
    --partner-blue: #1c3f8f;
  }
  * { margin: 0; padding: 0; box-sizing: border-box; }
  html, body { width: 927px; height: 1200px; overflow: hidden; background: var(--white); }
  .flyer {
    position: relative; width: 927px; height: 1200px; overflow: hidden;
    font-family: "Alegreya", Georgia, serif; color: var(--ink); background: var(--white);
  }
  .hero-photo {
    position: absolute; left: 0; top: 0; width: 927px; height: 256px;
    background: linear-gradient(180deg, #12307a 0%, #2a5a9e 45%, #1e3c5c 78%, #2f6b3a 100%);
  }
  .intro {
    position: absolute; left: 60px; top: 44px; width: 807px;
    color: var(--white); font-size: 18.5px; line-height: 29px; text-align: center;
    text-shadow: 0 1px 3px rgba(0,0,0,.55);
  }
  .partner-panel {
    position: absolute; left: 160px; top: 206px; width: 606px; height: 80px;
    background: var(--white); border-radius: 14px;
    box-shadow: 0 2px 6px rgba(0,0,0,.18);
    display: flex; align-items: center; justify-content: space-around;
  }
  .partner { display: flex; align-items: center; gap: 10px; font-size: 22px; font-weight: 700; }
  .partner .mark { width: 26px; height: 26px; }
  .partner--heritage { color: var(--partner-blue); }
  .partner--heritage .mark { background: var(--partner-blue); border-radius: 50%; }
  .partner--larkin { color: var(--partner-red); }
  .partner--larkin .mark { background: var(--partner-red); }
  .shapes { position: absolute; left: 0; top: 0; }
  .section-title {
    position: absolute; left: 22px; top: 346px;
    color: var(--white); font-size: 31px; font-weight: 700;
  }
  .inclusion {
    position: absolute; font-size: 20px; line-height: 21px; padding-left: 26px;
  }
  .inclusion::before {
    content: ""; position: absolute; left: 0; top: 6px; width: 9px; height: 9px; background: var(--ink);
  }
  .col-left { left: 11px; width: 460px; }
  .col-right { left: 493px; width: 430px; }
  .city-photo { position: absolute; left: 0; top: 0; }
  .footer {
    position: absolute; left: 0; top: 1136px; width: 927px; height: 48px;
    background: var(--brand-blue); color: var(--white);
    font-size: 19px; display: flex; align-items: center; justify-content: center;
  }
</style>
</head>
<body>
<div class="flyer">
  <div class="hero-photo" role="img" aria-label="Evening photo of a historic German riverside city with bridge, towers and domes"></div>
  <p class="intro">Daniel Marsh partnered with Heritage Crest Tours &amp; Music Festivals to bring you and experience of a Lifetime. With over 100 years of combined educational student travel expertise , Heritage Crest Tours, powered by Larkin Tours, brings unparalleled tour experiences for you and your students.</p>

  <div class="partner-panel">
    <div class="partner partner--heritage"><span class="mark"></span>Heritage Crest</div>
    <div class="partner partner--larkin"><span class="mark"></span>Larkin Tours</div>
  </div>

  <svg class="shapes" width="927" height="1200" viewBox="0 0 927 1200" aria-hidden="true">
    <polygon points="0,318 927,392 927,394 0,394" fill="var(--brand-blue)"/>
    <polygon points="0,732 927,732 927,792 0,740" fill="var(--brand-blue)"/>
  </svg>

  <svg class="city-photo" width="927" height="1200" viewBox="0 0 927 1200" role="img" aria-label="Twilight photo of the Dresden skyline with domes, spires and boats on the river">
    <defs>
      <linearGradient id="dusk" x1="0" y1="0" x2="0" y2="1">
        <stop offset="0" stop-color="#2bb3ea"/>
        <stop offset="0.5" stop-color="#1f6fc0"/>
        <stop offset="0.75" stop-color="#1a2f6a"/>
        <stop offset="1" stop-color="#13204a"/>
      </linearGradient>
    </defs>
    <polygon points="0,772 927,830 927,1124 0,1124" fill="url(#dusk)"/>
  </svg>

  <h2 class="section-title">Trip Inclusions:</h2>

  <p class="inclusion col-left" style="top:414px">Roundtrip Airfare from Houston</p>
  <p class="inclusion col-left" style="top:456px">13 Nights Accomodations, 3 Star Hotels with A/C</p>
  <p class="inclusion col-left" style="top:499px">Daily Breakfast</p>
  <p class="inclusion col-left" style="top:541px">Access to rehearsal sessions</p>
  <p class="inclusion col-left" style="top:584px">Pirvate Luxury Coach Transfer Services for airport transfers and day tours to Berlin, Weimar and Dresden &amp; Prague.</p>
  <p class="inclusion col-left" style="top:668px">Professional Local Guides for for City Tours in: Berlin, Weimar, Dresden &amp; Prague</p>

  <p class="inclusion col-right" style="top:414px">Entrance Fees to: House of Lukas Brenner, Franz Adler, Otto Weil in Weimar, Lutheran</p>
  <p class="inclusion col-right" style="top:478px">Frauenkirche &amp; Alte Meister Gallery in the Zwiner Palace in Dresend, and Cathedral and Golden</p>
  <p class="inclusion col-right" style="top:563px">Lane in Prague</p>
  <p class="inclusion col-right" style="top:605px">All Applicable Taxes and Gratuities for Included Services, Guides, and Drivers</p>
  <p class="inclusion col-right" style="top:668px">$2 Million in Professional Liability Insurance 24-hour Travel Support Staff</p>

  <div class="footer">For more information contact Dr. Marsh at daniel.marsh@example.edu</div>
</div>
</body>
</html>
```